VelTrova an innovative way to connect sellers with car dealers

The idea is a site that connects consumers that want to sell thier cars with a dealer network that is ready to buy.

**I just added 9/26 a POSSIBLE logo. Dont feel obligated to use this or design off of it.

The first goal is to provide a place where people can SEAMLESSLY list their vechile for sale to a car dealership network. We are looking for people that want to get more for their car than trading it in allows but DONT want to go through the hassel of listing and selling their car on their own. The dont want to deal with people reaching out, showing the vechile, and the risk assocated with retailing a valuable item to the general public. That said these people dont want to just trade their car wholesale and buy retail. These are the people that that do to a place like AutoPlenz to sell their car directly. However AutoPlenz is just one dealer.

The second fuction of the site allows dealers to view the vechiles that have been listed especilaly the ones in thier market.

I would like to add that I am looking for real images. No cartoon or animation. Upmarket but friendly.

I have attached a detailed document to help.

Target Market(s)

People that want to sell cars and dealers that want to buy cars

Industry/Entity Type

Automotive

Requirements
Must have
• The pages listed in the document
Should not have
• No cartoon or animated images

```html
<!DOCTYPE html>
<html lang="en">
<head>
<meta charset="utf-8">
<title>VelTrova — Sell Your Car, Hassle Free</title>
<link href="https://fonts.googleapis.com/css2?family=Roboto:wght@400;500;700;900&display=swap" rel="stylesheet">
<style>
:root{
  --blue:#1ea0dc;
  --blue-deep:#1469ad;
  --ink:#2f3338;
  --ink-soft:#5a5f66;
  --muted:#7b8088;
  --line:#e6e8eb;
  --paper:#ffffff;
  --panel-shadow:0 6px 24px rgba(0,0,0,.10);
  --dark:#3a3a3c;
}
*{box-sizing:border-box;margin:0;padding:0}
html,body{width:1200px;height:5222px;overflow:hidden}
body{position:relative;background:var(--paper);font-family:"Roboto",Arial,sans-serif;color:var(--ink)}
.abs{position:absolute}
.accent{color:var(--blue)}

/* CTA button */
.cta{position:absolute;display:flex;align-items:center;height:60px;text-decoration:none}
.cta-body{height:100%;flex:1;display:flex;align-items:center;justify-content:center;color:#fff;font-weight:700;font-size:19px;letter-spacing:.3px;
  background:linear-gradient(90deg,var(--blue),var(--blue-deep));clip-path:polygon(22px 0,100% 0,calc(100% - 22px) 100%,0 100%)}
.cta-stripe{width:14px;height:100%;margin-left:6px;background:var(--blue-deep);clip-path:polygon(70% 0,100% 0,30% 100%,0 100%)}

/* Header */
.hero{position:absolute;left:0;top:0;width:1200px;height:712px;
  background:linear-gradient(180deg,#4a4744 0%,#6b6158 30%,#3a3735 70%,#1f1e1e 100%)}
.hero-car{position:absolute;left:380px;top:240px;width:760px;height:470px;border-radius:50% 50% 20% 20%;
  background:radial-gradient(ellipse at 50% 55%,#2a2b2e 0%,#1a1b1d 55%,rgba(26,27,29,0) 72%)}
.brand{position:absolute;left:104px;top:24px;display:flex;align-items:center;gap:10px;color:#fff;font-weight:700;font-size:26px}
.brand-dot{width:16px;height:16px;border-radius:50%;background:var(--blue)}
.nav{position:absolute;top:32px;right:108px;display:flex;gap:44px;color:#fff;font-size:15px;font-weight:500}
.nav span{display:flex;align-items:center;gap:8px}
.hero-title{position:absolute;left:101px;top:220px;color:#fff;font-weight:900;font-size:52px;line-height:64px;letter-spacing:.5px}

/* Brand strip */
.brand-strip{position:absolute;top:774px;left:62px;width:1076px;height:50px;display:flex;align-items:center;justify-content:space-between}
.arrow-box{width:36px;height:30px;border:1px solid #c9ccd0;display:flex;align-items:center;justify-content:center}
.make{font-size:17px;font-weight:700;color:#6f747a;letter-spacing:1.5px}

/* Section titles */
.section-title{position:absolute;left:0;width:1200px;text-align:center;font-weight:700;font-size:38px;color:var(--ink)}

/* Model cards */
.model-card{position:absolute;top:1048px;width:493px;height:815px;background:#fff;box-shadow:var(--panel-shadow)}
.model-photo{position:absolute;left:35px;top:57px;width:385px;height:182px;border-radius:40% 45% 12% 12%}
.model-name{position:absolute;left:50px;top:268px;font-size:28px;font-weight:700;letter-spacing:8px}
.model-price{position:absolute;left:50px;top:310px;font-size:19px;color:var(--muted);display:flex;gap:14px}
.model-price b{color:var(--ink-soft);margin-right:48px}
.model-trim{position:absolute;left:50px;top:362px;font-size:18px;font-weight:700}
.feature-list{position:absolute;left:48px;top:418px;list-style:none}
.feature-list li{display:flex;align-items:center;gap:10px;height:51.5px;font-size:18px;color:var(--ink-soft)}
.card-actions{position:absolute;left:27px;top:687px;display:flex;gap:6px}
.btn-dark,.btn-outline{width:230px;height:61px;display:flex;align-items:center;justify-content:center;font-weight:700;font-size:18px}
.btn-dark{background:var(--dark);color:#fff;clip-path:polygon(22px 0,100% 0,calc(100% - 22px) 100%,0 100%)}
.btn-outline{color:var(--ink);position:relative}
.btn-outline svg{position:absolute;inset:0}

/* Stats */
.stat{position:absolute;top:2157px;height:274px;background:#fff;box-shadow:var(--panel-shadow);text-align:center}
.stat-num{margin-top:80px;font-size:50px;font-weight:500;color:var(--blue)}
.stat-label{margin-top:18px;font-size:18px;color:var(--ink);line-height:22px}

/* About */
.about{position:absolute;left:0;top:2493px;width:1200px;height:990px;
  background:linear-gradient(180deg,#e3ecf2 0%,#f1f4f6 45%,#8e9ca8 55%,#3b4650 80%,#22282e 100%)}
.about-photo{position:absolute;left:0;top:500px;width:1200px;height:490px;
  background:radial-gradient(ellipse at 55% 55%,#1b6fd1 0%,#174f92 25%,rgba(40,55,70,0) 55%),linear-gradient(180deg,#9fb0bd 0%,#57646f 40%,#2c333a 100%)}
.about-title{position:absolute;left:124px;top:2576px;font-size:38px;font-weight:700;line-height:46px;color:var(--ink-soft)}
.about-text{position:absolute;left:124px;top:2690px;width:420px;font-size:18px;line-height:38px;color:var(--ink-soft)}
.acc-row{position:absolute;left:638px;width:437px;display:flex;align-items:center;gap:18px;font-weight:700;font-size:21px;color:var(--ink-soft)}
.acc-row .chev{margin-left:auto}
.acc-open{position:absolute;left:608px;top:2629px;width:491px;height:304px;background:#fff;box-shadow:var(--panel-shadow)}
.acc-open .acc-head{position:absolute;left:27px;top:22px;width:440px;display:flex;align-items:center;gap:8px;color:var(--blue);font-weight:700;font-size:21px}
.acc-open .acc-head .chev{margin-left:auto}
.acc-open p{position:absolute;left:30px;top:96px;width:440px;font-size:18px;line-height:38px;color:var(--ink-soft)}

/* Trust */
.people-photo{position:absolute;left:81px;top:3547px;width:507px;height:811px;
  background:linear-gradient(180deg,#f3f3f3 0%,#d9d9d9 60%,#bcbcbc 100%);border-radius:40px}
.trust-title{position:absolute;left:651px;top:3578px;font-size:38px;font-weight:700;line-height:48px;color:var(--ink)}
.trust-text{position:absolute;left:660px;width:370px;font-size:12px;line-height:22px;color:var(--ink-soft)}
.step-line{position:absolute;left:678px;top:3832px;width:2px;height:250px;background:var(--blue)}
.step-num{position:absolute;left:664px;width:28px;height:28px;border:1px solid var(--blue);background:#fff;color:var(--blue);font-size:16px;display:flex;align-items:center;justify-content:center}
.step{position:absolute;left:720px;width:330px}
.step h3{display:flex;align-items:center;gap:12px;font-size:18px;font-weight:700;color:var(--ink)}
.step p{margin-top:10px;font-size:12px;line-height:22px;color:var(--ink-soft)}

/* Clients */
.clients{position:absolute;left:0;top:4439px;width:1200px;height:720px;background:linear-gradient(180deg,#e4e5e6 0%,#f1f1f1 40%,#f6f6f6 100%)}
.quote-card{position:absolute;left:284px;top:4652px;width:632px;height:446px;background:#fff;box-shadow:var(--panel-shadow)}
.quote-mark{position:absolute;left:24px;top:10px;font-size:110px;font-weight:900;color:#c9ccd0;line-height:1}
.quote-text{position:absolute;left:47px;top:56px;width:540px;font-size:18px;line-height:33px;color:var(--ink-soft)}
.avatar{position:absolute;left:47px;top:357px;width:68px;height:68px;border-radius:50%;background:linear-gradient(135deg,#b9a792,#6e6257)}
.stars{position:absolute;left:150px;top:372px;display:flex;gap:6px}
.client-car{position:absolute;left:780px;top:4946px;width:375px;height:203px;border-radius:45% 45% 18% 18%;
  background:radial-gradient(ellipse at 50% 55%,#1c3fae 0%,#142c78 50%,rgba(20,44,120,0) 72%)}
.dots{position:absolute;left:548px;top:5097px;display:flex;gap:10px;align-items:center}
.dots span{width:12px;height:12px;border-radius:50%;background:#d5d8dc}
.dots .on{width:38px;border-radius:7px;background:var(--blue)}
.footer{position:absolute;left:0;top:5159px;width:1200px;height:63px;background:var(--dark);color:#cfd1d4;font-size:10px;display:flex;align-items:center;justify-content:center}
</style>
</head>
<body>

<!-- Header / hero -->
<section class="hero" role="img" aria-label="Dark sports car on a desert road at sunset">
  <div class="hero-car"></div>
</section>
<div class="brand"><span class="brand-dot"></span>VelTrova</div>
<nav class="nav">
  <span>What we do</span>
  <span>Dealership Login</span>
  <span><svg width="18" height="18" viewBox="0 0 24 24" fill="none" stroke="#fff" stroke-width="2"><path d="M14 3h6v18h-6M3 12h12M11 8l4 4-4 4"/></svg>Sign in</span>
  <span><svg width="16" height="16" viewBox="0 0 24 24" fill="none" stroke="#fff" stroke-width="2"><path d="M5 3h4l2 5-3 2a12 12 0 0 0 6 6l2-3 5 2v4a2 2 0 0 1-2 2A18 18 0 0 1 3 5a2 2 0 0 1 2-2z"/></svg>1-555-010-2040</span>
</nav>
<h1 class="hero-title">SELL YOUR<br>CAR, HASSLE<br>FREE</h1>
<a class="cta" style="left:101px;top:489px;width:380px"><span class="cta-body">SELL YOUR CAR NOW</span><span class="cta-stripe"></span><span class="cta-stripe"></span></a>

<!-- Brand strip -->
<div class="brand-strip">
  <span class="arrow-box"><svg width="16" height="12" viewBox="0 0 16 12" fill="none" stroke="#555" stroke-width="1.5"><path d="M15 6H2M6 1 1 6l5 5"/></svg></span>
  <span class="make">FERROWEN</span>
  <span class="make">JAVELLE</span>
  <span class="make">HYVORA</span>
  <span class="make">HONDRIX</span>
  <span class="make">ASTRELLE</span>
  <span class="make">SUVARO</span>
  <span class="make">MARVESSI</span>
  <span class="arrow-box"><svg width="16" height="12" viewBox="0 0 16 12" fill="none" stroke="#555" stroke-width="1.5"><path d="M1 6h13M10 1l5 5-5 5"/></svg></span>
</div>

<!-- Models -->
<h2 class="section-title" style="top:958px">NORDEO MODELS <span class="accent">AVAILABLE</span></h2>

<article class="model-card" style="left:101px">
  <div class="model-photo" role="img" aria-label="Blue sedan, front three-quarter view" style="background:radial-gradient(ellipse at 50% 55%,#2446b8 0%,#1a2f7c 55%,rgba(26,47,124,0) 75%)"></div>
  <div class="model-name">NORDEO</div>
  <div class="model-price"><span>FROM</span><b>$80000</b><span>AS SHOWN</span><b style="margin:0">$80000</b></div>
  <div class="model-trim">STANDARD FEATURED, PLUS</div>
  <ul class="feature-list">
    <li><svg width="14" height="12" viewBox="0 0 14 12" fill="none" stroke="#1ea0dc" stroke-width="1.8"><path d="M1 6l4 4 8-9"/></svg>Driver Awareness Package</li>
    <li><svg width="14" height="12" viewBox="0 0 14 12" fill="none" stroke="#1ea0dc" stroke-width="1.8"><path d="M1 6l4 4 8-9"/></svg>Rear Camera</li>
    <li><svg width="14" height="12" viewBox="0 0 14 12" fill="none" stroke="#1ea0dc" stroke-width="1.8"><path d="M1 6l4 4 8-9"/></svg>Color Head-Up Display</li>
    <li><svg width="14" height="12" viewBox="0 0 14 12" fill="none" stroke="#1ea0dc" stroke-width="1.8"><path d="M1 6l4 4 8-9"/></svg>Driver Awareness Package</li>
    <li><svg width="14" height="12" viewBox="0 0 14 12" fill="none" stroke="#1ea0dc" stroke-width="1.8"><path d="M1 6l4 4 8-9"/></svg>Available Sports Edition</li>
  </ul>
  <div class="card-actions">
    <span class="btn-dark">MORE DETAILS</span>
    <span class="btn-outline"><svg width="230" height="61" viewBox="0 0 230 61"><polygon points="22,1 229,1 208,60 1,60" fill="none" stroke="#3a3a3c" stroke-width="1.5"/></svg>PRICE DETAILS</span>
  </div>
</article>

<article class="model-card" style="left:608px">
  <div class="model-photo" role="img" aria-label="Silver sedan, front three-quarter view" style="background:radial-gradient(ellipse at 50% 55%,#a9acb1 0%,#7d8086 55%,rgba(125,128,134,0) 75%)"></div>
  <div class="model-name">NORDEO</div>
  <div class="model-price"><span>FROM</span><b>$80000</b><span>AS SHOWN</span><b style="margin:0">$80000</b></div>
  <div class="model-trim">STANDARD FEATURED, PLUS</div>
  <ul class="feature-list">
    <li><svg width="14" height="12" viewBox="0 0 14 12" fill="none" stroke="#1ea0dc" stroke-width="1.8"><path d="M1 6l4 4 8-9"/></svg>Driver Awareness Package</li>
    <li><svg width="14" height="12" viewBox="0 0 14 12" fill="none" stroke="#1ea0dc" stroke-width="1.8"><path d="M1 6l4 4 8-9"/></svg>Rear Camera</li>
    <li><svg width="14" height="12" viewBox="0 0 14 12" fill="none" stroke="#1ea0dc" stroke-width="1.8"><path d="M1 6l4 4 8-9"/></svg>Color Head-Up Display</li>
    <li><svg width="14" height="12" viewBox="0 0 14 12" fill="none" stroke="#1ea0dc" stroke-width="1.8"><path d="M1 6l4 4 8-9"/></svg>Driver Awareness Package</li>
    <li><svg width="14" height="12" viewBox="0 0 14 12" fill="none" stroke="#1ea0dc" stroke-width="1.8"><path d="M1 6l4 4 8-9"/></svg>Available Sports Edition</li>
  </ul>
  <div class="card-actions">
    <span class="btn-dark">MORE DETAILS</span>
    <span class="btn-outline"><svg width="230" height="61" viewBox="0 0 230 61"><polygon points="22,1 229,1 208,60 1,60" fill="none" stroke="#3a3a3c" stroke-width="1.5"/></svg>PRICE DETAILS</span>
  </div>
</article>

<a class="cta" style="left:420px;top:1930px;width:390px"><span class="cta-body">SELL YOUR CAR NOW</span><span class="cta-stripe"></span><span class="cta-stripe"></span></a>

<!-- Stats -->
<h2 class="section-title" style="top:2066px">OUR TRACK RECORD OF <span class="accent">SUCCESS</span></h2>
<div class="stat" style="left:101px;width:321px"><div class="stat-num">10,000+</div><div class="stat-label">CAR SOLD!</div></div>
<div class="stat" style="left:440px;width:320px"><div class="stat-num">99%</div><div class="stat-label">SATISFACTION RATE</div></div>
<div class="stat" style="left:776px;width:323px"><div class="stat-num">70%</div><div class="stat-label">CUSTOMER ACCEPT<br>FIRST OFFER</div></div>

<!-- About -->
<section class="about">
  <div class="about-photo" role="img" aria-label="Blue sports car parked on a hillside road"></div>
</section>
<h2 class="about-title">WE ARE BEST<br><span class="accent">CAR</span>SELLER</h2>
<p class="about-text">Discover the ultimate platform for buying and selling cars with [Company Name]! Experience instant offers, a vast inventory, and a hassle-free process.</p>
<a class="cta" style="left:120px;top:2921px;width:390px"><span class="cta-body">SELL YOUR CAR NOW</span><span class="cta-stripe"></span><span class="cta-stripe"></span></a>

<div class="acc-row" style="top:2554px">
  <svg width="40" height="40" viewBox="0 0 40 40" fill="none" stroke="#4a4f56" stroke-width="2"><circle cx="20" cy="20" r="18"/><path d="M15 15a5 5 0 1 1 7 4.5c-1.5.8-2 1.5-2 3.5M20 27v1"/></svg>
  WHO ARE WE?
  <svg class="chev" width="18" height="10" viewBox="0 0 18 10" fill="none" stroke="#4a4f56" stroke-width="2"><path d="M1 1l8 8 8-8"/></svg>
</div>
<div class="acc-open">
  <div class="acc-head">
    <svg width="56" height="56" viewBox="0 0 56 56" fill="none" stroke="#1ea0dc" stroke-width="2"><circle cx="28" cy="28" r="26"/><path d="M17 32l3-9h16l3 9v6H17zM20 38v3M36 38v3M17 32h22"/></svg>
    WHAT WE DO?
    <svg class="chev" width="18" height="10" viewBox="0 0 18 10" fill="none" stroke="#1ea0dc" stroke-width="2"><path d="M1 9l8-8 8 8"/></svg>
  </div>
  <p>We make selling your car quick and stress-free. With instant offers, transparent pricing, and no hidden fees, you'll get a fair deal fast. We take care of paperwork and provide free pickup, ensuring a seamless experience from start to finish.</p>
</div>
<div class="acc-row" style="top:2960px">
  <svg width="40" height="42" viewBox="0 0 40 42" fill="none" stroke="#4a4f56" stroke-width="2"><path d="M4 2h26v20M4 2v38h18M10 12h16M10 20h16M10 28h8M24 34l5 5 9-11"/></svg>
  HOW WE DO IT?
  <svg class="chev" width="18" height="10" viewBox="0 0 18 10" fill="none" stroke="#4a4f56" stroke-width="2"><path d="M1 1l8 8 8-8"/></svg>
</div>

<!-- Trust -->
<div class="people-photo" role="img" aria-label="Two businessmen shaking hands"></div>
<h2 class="trust-title">DEALERS AND BUYERS<br>YOU <span class="accent">CAN TRUST</span></h2>
<p class="trust-text" style="top:3680px">We are committed to providing quality vehicles and exceptional service. Our experienced team ensures transparency and reliability, making your buying and selling experience seamless and stress-free.</p>
<div class="step-line"></div>
<div class="step-num" style="top:3808px">1</div>
<div class="step-num" style="top:3932px">2</div>
<div class="step-num" style="top:4062px">3</div>
<div class="step" style="top:3802px">
  <h3><svg width="40" height="30" viewBox="0 0 40 30" fill="none" stroke="#3a3a3c" stroke-width="2"><path d="M2 4h22v18H2zM24 10h8l6 7v5H24M9 26a3 3 0 1 0 0-.1M31 26a3 3 0 1 0 0-.1"/></svg>WE DELIEVR ANYWHERE</h3>
  <p>We deliver your dream car anywhere you are, ensuring convenience and satisfaction with every purchase</p>
</div>
<div class="step" style="top:3926px">
  <h3><svg width="38" height="32" viewBox="0 0 38 32" fill="none" stroke="#3a3a3c" stroke-width="2"><path d="M2 14l8-10 8 4 6-3 12 9-12 12-10-6-6 4zM18 8l-6 8 4 3 6-6"/></svg>BEST DEALS</h3>
  <p>We are the best dealer, ensuring convenience and satisfaction with every purchase</p>
</div>
<div class="step" style="top:4058px">
  <h3><svg width="32" height="32" viewBox="0 0 32 32" fill="none" stroke="#3a3a3c" stroke-width="2.5"><circle cx="16" cy="16" r="13"/><path d="M7 25L25 7"/></svg>NO PUSHY SALES</h3>
  <p>We operate differently to a dealership and put our customers first!</p>
</div>
<p class="trust-text" style="top:4186px">We prioritize your security, ensuring every deal is safe, transparent, and hassle-free for our customers.</p>
<a class="cta" style="left:647px;top:4281px;width:392px"><span class="cta-body">SELL YOUR CAR NOW</span><span class="cta-stripe"></span><span class="cta-stripe"></span></a>

<!-- Clients -->
<section class="clients" role="img" aria-label="Faint city street backdrop"></section>
<h2 class="section-title" style="top:4560px">OUR HAPPY <span class="accent">CLIENTS</span></h2>
<article class="quote-card">
  <div class="quote-mark">“</div>
  <p class="quote-text">Selling my car with VelTrova was an incredible experience. I was initially apprehensive about the process, but they made it so simple! I entered my car details online and received a great offer within minutes. The team was professional, answering all my questions and handling the paperwork seamlessly. I received my payment the same day! I couldn't have asked for a better experience</p>
  <div class="avatar" role="img" aria-label="Client portrait"></div>
  <div class="stars">
    <svg width="150" height="26" viewBox="0 0 150 26" fill="#f4c20d"><g id="s"><path d="M13 1l3.6 7.6 8.2 1-6 5.7 1.6 8.2L13 19.5 5.6 23.5l1.6-8.2-6-5.7 8.2-1z"/></g><use href="#s" x="30"/><use href="#s" x="60"/><use href="#s" x="90"/><use href="#s" x="120"/></svg>
  </div>
</article>
<div class="client-car" role="img" aria-label="Blue coupe, front three-quarter view"></div>
<div class="dots"><span class="on"></span><span></span><span></span><span></span></div>

<footer class="footer">Copyright2024 VelTrova. All Rights Reserved</footer>

</body>
</html>
```